Brisk Meadow Builders needs an updated flyer

Instructions are in a .pdf called "Instructions. All photos and logos are included along with the original flyer in .ai

We are looking for a fresh design that promotes sustainability.

```html
<!DOCTYPE html>
<html lang="en">
<head>
<meta charset="utf-8">
<title>Prairie Barn House Mini – Brisk Meadow Builders</title>
<link href="https://fonts.googleapis.com/css2?family=Cabin:wght@400;500;600;700&display=swap" rel="stylesheet">
<style>
  :root{
    --green:#52ab4f;
    --green-dark:#3d8a3c;
    --green-title:#3f8d3c;
    --orange:#f7a823;
    --orange-deep:#f39a1f;
    --ink:#111111;
    --white:#ffffff;
    --mist-top:#b9c4cb;
    --mist-bottom:#eef1f3;
  }
  *{margin:0;padding:0;box-sizing:border-box}
  html,body{width:927px;height:1200px;overflow:hidden;background:#fff}
  body{font-family:"Cabin",Arial,sans-serif;color:var(--ink)}
  .flyer{position:relative;width:927px;height:1200px;overflow:hidden}
  .abs{position:absolute;white-space:nowrap}

  /* hero */
  .hero{position:absolute;left:0;top:0;width:927px;height:410px}
  .brand{left:606px;top:104px;display:flex;align-items:center;gap:8px;font-weight:700;font-size:25px;color:var(--green-title)}
  .brand-dot{width:14px;height:14px;border-radius:50%;background:var(--orange)}
  .title-the{left:559px;top:180px;font-size:34px;font-weight:500;color:var(--green)}
  .title-main{left:521px;top:210px;font-size:68px;line-height:59px;font-weight:700;color:var(--orange);letter-spacing:-1.5px}
  .tagline{left:541px;top:333px;font-size:22px;font-weight:600;color:var(--green)}

  /* features band */
  .features{position:absolute;left:0;top:410px;width:927px;height:308px;background:linear-gradient(135deg,var(--green) 0%,var(--green-dark) 100%)}
  .price{position:absolute;left:574px;top:390px;width:353px;height:156px;background:linear-gradient(180deg,var(--orange),var(--orange-deep));border-top-left-radius:58px}
  .price-label{left:56px;top:36px;font-size:27px;line-height:26px;font-weight:700;color:var(--ink)}
  .price-value{left:56px;top:84px;font-size:56px;line-height:60px;font-weight:700;color:var(--ink)}
  .features-heading{left:62px;top:448px;font-size:48px;font-weight:700;color:var(--white)}
  .feature{position:absolute;display:flex;gap:9px;color:var(--white);font-size:18px;line-height:17.5px;letter-spacing:-0.2px}
  .feature svg{flex:none;width:29px;height:27px;margin-top:-7px}

  /* photo strip */
  .photo{position:absolute;top:718px;height:180px}

  /* bottom */
  .options-panel{position:absolute;left:0;top:898px;width:464px;height:302px;background:linear-gradient(180deg,var(--mist-top),var(--mist-bottom))}
  .uses-panel{position:absolute;left:464px;top:898px;width:463px;height:302px;background:linear-gradient(135deg,var(--green-dark),var(--green))}
  .options-heading{left:55px;top:906px;font-size:40px;font-weight:700;color:var(--green-title)}
  .options-list{left:55px;top:962px;list-style:none;font-size:17.5px;line-height:17.3px;color:var(--ink)}
  .options-list li::before{content:"• ";font-size:12px;vertical-align:2px}
  .uses-heading{left:500px;top:906px;font-size:40px;font-weight:700;color:var(--orange)}
  .uses-list{left:509px;top:962px;list-style:none;font-size:17.5px;line-height:17.3px;color:var(--white)}
  .uses-list b{color:var(--orange)}
  .uses-list .indent{padding-left:13px}
  .cta-pill{position:absolute;left:33px;top:1075px;width:845px;height:48px;border-radius:24px;background:var(--orange);display:flex;align-items:center;justify-content:center;font-size:31px;font-weight:700;color:var(--ink);letter-spacing:-0.6px}
  .contact-phone{left:57px;top:1138px;font-size:34px;font-weight:700;color:var(--ink);letter-spacing:-0.5px;word-spacing:10px}
  .contact-web{left:477px;top:1143px;font-size:25px;font-weight:700;color:var(--orange)}
</style>
</head>
<body>
<main class="flyer">
  <svg width="0" height="0" style="position:absolute">
    <symbol id="tick" viewBox="0 0 29 27">
      <rect x="1.5" y="7" width="18" height="18" fill="none" stroke="#fff" stroke-width="2.6"/>
      <path d="M5 14 L11 21 L27 2" fill="none" stroke="#fff" stroke-width="3.2" stroke-linecap="round" stroke-linejoin="round"/>
    </symbol>
  </svg>

  <svg class="hero" viewBox="0 0 927 410">
    <defs>
      <linearGradient id="heroPhoto" x1="0" y1="0" x2="0" y2="1">
        <stop offset="0" stop-color="#8fb3d6"/>
        <stop offset="0.45" stop-color="#5c7f48"/>
        <stop offset="1" stop-color="#6e6b66"/>
      </linearGradient>
      <clipPath id="heroClip"><rect width="927" height="410"/></clipPath>
    </defs>
    <rect width="927" height="410" fill="url(#heroPhoto)" role="img" aria-label="Photo of the white board-and-batten vending tiny house on a tandem trailer with a wooden porch deck"/>
    <g clip-path="url(#heroClip)">
      <circle cx="784" cy="209" r="310" fill="#f7a823"/>
      <rect x="784" y="0" width="143" height="410" fill="#f7a823"/>
      <circle cx="784" cy="209" r="296" fill="#ffffff"/>
      <rect x="784" y="0" width="143" height="410" fill="#ffffff"/>
    </g>
  </svg>

  <div class="abs brand"><span class="brand-dot"></span>Brisk Meadow Builders</div>
  <div class="abs title-the">The</div>
  <h1 class="abs title-main">Prairie Barn<br>House Mini</h1>
  <p class="abs tagline">Luxury, mobile vending house</p>

  <section class="features">
  </section>
  <div class="price">
    <p class="abs price-label">Base price<br>starting at just:</p>
    <p class="abs price-value">$65,000</p>
  </div>
  <h2 class="abs features-heading">Base unit features:</h2>

  <div class="feature" style="left:63px;top:518px"><svg><use href="#tick"/></svg><span>Trailer features tandem wheels w/brakes.</span></div>
  <div class="feature" style="left:63px;top:548px"><svg><use href="#tick"/></svg><span>Steel frame construction for fire retardation<br>safety and weight reduction.</span></div>
  <div class="feature" style="left:63px;top:595px"><svg><use href="#tick"/></svg><span>“100% Off grid with solar &amp; up to 20 KWH’s<br>of lithium battery storage allowing trailer<br>to be used in places not accessible by<br>traditional trailers.</span></div>
  <div class="feature" style="left:63px;top:677px"><svg><use href="#tick"/></svg><span>Custom interiors to suit various uses.</span></div>

  <div class="feature" style="left:478px;top:556px"><svg><use href="#tick"/></svg><span>60 Gallon water supply tank.</span></div>
  <div class="feature" style="left:478px;top:584px"><svg><use href="#tick"/></svg><span>70 Gallon waste water tank.</span></div>
  <div class="feature" style="left:478px;top:616px"><svg><use href="#tick"/></svg><span>Cupboards, cabinets &amp; four stainless steel sinks.</span></div>
  <div class="feature" style="left:478px;top:646px"><svg><use href="#tick"/></svg><span>60” Gas shock serving window.</span></div>
  <div class="feature" style="left:478px;top:677px"><svg><use href="#tick"/></svg><span>Multiple sizes from 12’, 16’, 20’ &amp; 24’ long.</span></div>

  <div class="photo" style="left:0;width:288px;background:linear-gradient(180deg,#cfd9e2 0%,#4f7a3c 35%,#7d7c79 100%)" role="img" aria-label="Photo of the vending house with rooftop solar panels, front three-quarter view"></div>
  <div class="photo" style="left:288px;width:371px;background:linear-gradient(180deg,#d6dde4 0%,#466f36 40%,#5f6263 100%)" role="img" aria-label="Photo of the vending house parked on an asphalt lot surrounded by trees"></div>
  <div class="photo" style="left:659px;width:268px;background:linear-gradient(180deg,#9fbad6 0%,#55803f 45%,#6d6d6b 100%)" role="img" aria-label="Photo of the vending house side view showing the open serving window"></div>

  <div class="options-panel"></div>
  <div class="uses-panel"></div>
  <h2 class="abs options-heading">Available options:</h2>
  <ul class="abs options-list">
    <li>HVAC - Northwind Mini Split</li>
    <li>Cooler / Glass front commercial refrigerator</li>
    <li>Upper lofts storage area</li>
    <li>Signage and graphics</li>
    <li>Ice machine</li>
    <li>3 foot fold down porch deck</li>
  </ul>
  <h2 class="abs uses-heading">Use cases:</h2>
  <ul class="abs uses-list">
    <li><b>a) Food:</b> Lemonade, coffee, pizza, cookies,</li>
    <li class="indent">doughnuts, farm to table etc.”</li>
    <li><b>b) Retail:</b> Grocery / convenience, clothing,</li>
    <li class="indent">watches, jewelry, flowers, crafts, art.</li>
    <li><b>c) Fundraisers:</b> Boy/Girl sports, non profits</li>
  </ul>

  <div class="cta-pill">Need a custom branded solution for your business?</div>
  <p class="abs contact-phone">Let’s talk! 704-555-0148</p>
  <p class="abs contact-web">www.BriskMeadowBuilders.com</p>
</main>
</body>
</html>
```